Newspaper Ad for Front page strip

Halvoria Quick Lending is a micro lender operating in the Caribbean. This ad is for our Trinidad and Tobago location.
Would like to design a catchy banner ad for the front page of a daily newspaper. The ad should capture 1) that we offer unsecured loans up to $40,000. 2) customer can apply online or over the phone 3) that the process is quick.
We have included the a snapshot of our Instagram posts as well as the newspaper location and size of the ad.
We have booked this ad spot for the year so the more engaging we can make it the better. Maybe we can do a series of ads or weekly storyline . Let’s be creative.
https://www.instagram.com/halvoriaquicklending/
www.halvoriaquick lending.example
Target Market(s)
Mass population.
Industry/Entity Type
Banking
Look and feel

```html
<!DOCTYPE html>
<html lang="en">
<head>
<meta charset="UTF-8">
<title>Halvoria Quick Lending – Front Page Strip</title>
<link href="https://fonts.googleapis.com/css2?family=Oswald:wght@600;700&family=Montserrat:wght@600;700;800&display=swap" rel="stylesheet">
<style>
  :root{
    --page:#ffffff;
    --brand-red:#e0232d;
    --blue-deep:#1553a6;
    --blue-mid:#2a74c9;
    --blue-light:#3d8ad8;
    --sun:#f7c31a;
    --orange:#f06a0c;
    --orange-light:#ff9a2e;
    --white:#ffffff;
    --photo-light:#efefee;
    --photo-mid:#d6d3d0;
  }
  *{margin:0;padding:0;box-sizing:border-box}
  html,body{width:769px;height:1200px;overflow:hidden;background:var(--page)}
  .canvas{position:relative;width:769px;height:1200px}
  .strip-ad{
    position:absolute;left:234px;top:39px;width:300px;height:1122px;
    background:var(--white);overflow:hidden;
    box-shadow:2px 3px 6px rgba(0,0,0,.35);
    font-family:"Montserrat",Arial,sans-serif;text-align:center;
  }
  .brand-block{position:absolute;left:0;top:0;width:300px;height:175px;
    display:flex;align-items:center;justify-content:center}
  .brand-name{font-family:"Montserrat",Arial,sans-serif;font-weight:800;
    color:var(--brand-red);font-size:28px;line-height:1.15;letter-spacing:1px}
  .hero-photo{position:absolute;left:0;top:175px;width:300px;height:260px;
    background:linear-gradient(160deg,var(--photo-light) 0%,var(--photo-mid) 60%,#c9b9b1 100%)}
  .swoosh{position:absolute;left:0;top:395px;width:300px;height:60px}
  .offer-panel{position:absolute;left:0;top:425px;width:300px;height:569px;
    background:linear-gradient(180deg,var(--blue-deep) 0%,var(--blue-mid) 45%,var(--blue-light) 65%,var(--blue-deep) 100%)}
  .line{position:absolute;left:0;width:300px;white-space:nowrap}
  .headline{font-family:"Oswald",Impact,sans-serif;font-weight:700;font-size:68px;line-height:68px;
    text-shadow:1px 2px 2px rgba(0,0,0,.3);transform:scaleY(1.05)}
  .headline.white{color:var(--white)}
  .headline.yellow{color:var(--sun)}
  .offer-text{font-weight:700;font-size:27px;line-height:32px;color:var(--white)}
  .offer-text.yellow{color:var(--sun)}
  .amount-button{position:absolute;left:40px;top:751px;width:220px;height:70px;
    border-radius:6px;background:linear-gradient(180deg,var(--orange-light),var(--orange));
    box-shadow:0 3px 4px rgba(0,0,0,.35);
    font-family:"Oswald",Impact,sans-serif;font-weight:700;font-size:46px;line-height:70px;
    color:var(--white);text-shadow:1px 2px 2px rgba(0,0,0,.35)}
  .apply-icon{position:absolute;left:120px;top:839px;width:60px;height:60px}
  .apply-text{font-weight:800;font-size:21px;line-height:30px;color:var(--white)}
  .apply-text .hl{color:var(--sun)}
  .speed-band{position:absolute;left:0;top:994px;width:300px;height:64px;background:var(--white);
    padding-top:6px;font-weight:800;font-size:21px;line-height:24px;color:var(--brand-red)}
  .web-band{position:absolute;left:0;top:1058px;width:300px;height:64px;background:var(--blue-deep);
    font-weight:700;font-size:12.5px;line-height:50px;color:var(--white)}
  .web-band .hl{color:var(--sun)}
</style>
</head>
<body>
<div class="canvas">
  <div class="strip-ad">
    <div class="brand-block"><span class="brand-name">THE HALVORIA<br>GROUP</span></div>

    <div class="hero-photo" role="img" aria-label="Photo of an excited young woman in red overalls pointing at a loan approval on her phone, in a bright home interior"></div>

    <div class="offer-panel"></div>
    <svg class="swoosh" viewBox="0 0 300 60" preserveAspectRatio="none" aria-hidden="true">
      <path d="M0 40 Q150 -10 300 12 L300 60 L0 60 Z" fill="#e0232d"/>
      <path d="M0 48 Q150 2 300 24 L300 60 L0 60 Z" fill="#1553a6"/>
    </svg>

    <div class="line headline white" style="top:452px">FINANCE</div>
    <div class="line headline yellow" style="top:517px">SERVICE</div>

    <div class="line offer-text yellow" style="top:596px">WE OFFER</div>
    <div class="line offer-text" style="top:632px">UNSECURED</div>
    <div class="line offer-text" style="top:670px">LOANS</div>
    <div class="line offer-text" style="top:708px">UP TO</div>

    <div class="amount-button">$40,000</div>

    <svg class="apply-icon" viewBox="0 0 60 60" aria-hidden="true">
      <circle cx="30" cy="30" r="28" fill="#f7c31a" stroke="#ffffff" stroke-width="2"/>
      <rect x="15" y="17" width="30" height="21" rx="2" fill="#1553a6"/>
      <rect x="19" y="21" width="10" height="3" fill="#f7c31a"/>
      <rect x="19" y="27" width="22" height="2" fill="#ffffff"/>
      <rect x="19" y="32" width="16" height="2" fill="#ffffff"/>
      <rect x="27" y="38" width="6" height="4" fill="#1553a6"/>
      <rect x="21" y="42" width="18" height="3" rx="1" fill="#1553a6"/>
    </svg>

    <div class="line apply-text" style="top:900px">customer can</div>
    <div class="line apply-text" style="top:930px"><span class="hl">apply online</span> or</div>
    <div class="line apply-text" style="top:960px">over the <span class="hl">phone</span></div>

    <div class="speed-band">that the process<br>is quick</div>

    <div class="web-band">www.halvoriaquick <span class="hl">lending</span>.example</div>
  </div>
</div>
</body>
</html>
```